Harlow Ridge Partners Business Cards

Design Business cards in a format where I can change the information and utilize a third party buisness card printing company

Contact Information for Business Card

Want Logo and Name on Back. Looking for Spot UV style shine on Logo. Probably Black background. Want smaller logo on front with contact details. Like rounded edges or something else interesting.

Requirements
Must have
• Strong masculine look.

```html
<!DOCTYPE html>
<html lang="en">
<head>
<meta charset="UTF-8">
<title>Harlow Ridge Partners – Business Cards</title>
<link href="https://fonts.googleapis.com/css2?family=Jost:wght@400;500&family=Oswald:wght@500&display=swap" rel="stylesheet">
<style>
  :root {
    --backdrop: #2b2b2b;
    --card: #1c1c1c;
    --card-edge: #262626;
    --ink: #f2f2f2;
    --ink-soft: #d6d6d6;
    --gloss: #5e5e5e;
    --icon: #9a9a9a;
  }
  * { margin: 0; padding: 0; box-sizing: border-box; }
  html, body {
    width: 1200px; height: 898px; overflow: hidden;
    background: var(--backdrop);
    font-family: "Jost", sans-serif;
  }
  .sheet {
    width: 1200px; height: 898px;
    display: flex; flex-direction: column;
    align-items: center; justify-content: center;
    gap: 40px;
  }
  .card {
    position: relative;
    width: 620px; height: 354px;
    background: var(--card);
    border: 1px solid var(--card-edge);
    box-shadow: 0 14px 30px rgba(0,0,0,0.45);
  }

  /* Back of card */
  .card-back .brand {
    position: absolute; left: 0; right: 0; top: 112px;
    display: flex; flex-direction: column; align-items: center; gap: 18px;
  }
  .brand-mark {
    width: 54px; height: 54px;
    background: var(--gloss);
  }
  .brand-name {
    font-family: "Jost", sans-serif;
    font-weight: 500;
    font-size: 30px;
    letter-spacing: 1px;
    color: var(--gloss);
  }
  .card-back .site {
    position: absolute; left: 0; right: 0; bottom: 34px;
    text-align: center;
    font-size: 15px; letter-spacing: 1.5px;
    color: var(--ink-soft);
  }

  /* Front of card */
  .person {
    position: absolute; left: 48px; top: 40px;
  }
  .person-name {
    font-family: "Oswald", sans-serif;
    font-weight: 500;
    font-size: 38px;
    line-height: 1;
    color: var(--ink);
    text-transform: uppercase;
  }
  .person-role {
    margin-top: 6px;
    font-size: 17px;
    color: var(--ink-soft);
  }
  .card-front .brand {
    position: absolute; right: 44px; top: 56px;
    display: flex; flex-direction: column; align-items: center; gap: 12px;
  }
  .card-front .brand-mark { width: 40px; height: 40px; }
  .card-front .brand-name { font-size: 22px; }

  .contacts {
    position: absolute; left: 48px; bottom: 40px;
    list-style: none;
    display: flex; flex-direction: column; gap: 6px;
  }
  .contacts li {
    display: flex; align-items: center; gap: 12px;
    font-size: 18px; letter-spacing: 1px;
    color: var(--ink-soft);
  }
  .contacts svg { width: 16px; height: 16px; flex: none; }
  .address {
    position: absolute; right: 44px; bottom: 40px;
    text-align: right;
    font-size: 18px; letter-spacing: 1px; line-height: 1.35;
    color: var(--ink-soft);
  }
</style>
</head>
<body>
<main class="sheet">

  <section class="card card-back" aria-label="Card back">
    <div class="brand">
      <div class="brand-mark"></div>
      <div class="brand-name">Harlow Ridge Partners</div>
    </div>
    <p class="site">www.yoursitename.com</p>
  </section>

  <section class="card card-front" aria-label="Card front">
    <div class="person">
      <h1 class="person-name">Daniel Ashford</h1>
      <p class="person-role">CEO &amp; Founder</p>
    </div>

    <div class="brand">
      <div class="brand-mark"></div>
      <div class="brand-name">Harlow Ridge Partners</div>
    </div>

    <ul class="contacts">
      <li>
        <svg viewBox="0 0 16 16" aria-hidden="true"><rect x="4" y="1" width="8" height="14" rx="1.5" fill="none" stroke="var(--icon)" stroke-width="1.4"/><line x1="7" y1="12.5" x2="9" y2="12.5" stroke="var(--icon)" stroke-width="1.4"/></svg>
        000 111 2223
      </li>
      <li>
        <svg viewBox="0 0 16 16" aria-hidden="true"><rect x="1" y="3" width="14" height="10" fill="var(--icon)"/><polyline points="1,3 8,9 15,3" fill="none" stroke="var(--card)" stroke-width="1.4"/></svg>
        urname@email.com
      </li>
      <li>
        <svg viewBox="0 0 16 16" aria-hidden="true"><circle cx="9.5" cy="6.5" r="4.5" fill="none" stroke="var(--icon)" stroke-width="1.6"/><line x1="6.3" y1="9.7" x2="1.5" y2="14.5" stroke="var(--icon)" stroke-width="1.8"/></svg>
        www.yoursitename.com
      </li>
    </ul>

    <p class="address">Your Street Address Here,<br>NewYork City, 1234</p>
  </section>

</main>
</body>
</html>
```